Dune Haulers Catalogue Template Design

We need a new fresh brand design for our business in the form of a catalogue layout. Dune Haulers is a Fuel transportation company and we have specialised tank trucks to deliver gasoline. The catalogue should provide a feeling of motion. Colours to be used: RED, GREY, BLACKWe like the use of parallelograms and geometric motion patterns. The Catalogue should provide a feeling of motion. We have included some notes on design concepts that we like. Please look at this brief as this will guide you in your design process.We will use this catalogue concept to design our company corporate identity. Final designs should communicate sophistication and success

```html
<!DOCTYPE html>
<html lang="en">
<head>
<meta charset="utf-8">
<title>Dune Haulers Catalogue Covers</title>
<link rel="stylesheet" href="https://fonts.googleapis.com/css2?family=Montserrat:wght@400;600;800;900&display=swap">
<style>
  :root{
    --red:#e3141d;
    --red-deep:#b90c14;
    --black:#1b1b1b;
    --grey:#6f6f6f;
    --grey-light:#ececec;
    --paper:#ffffff;
    --stage:#ffffff;
  }
  html,body{margin:0;padding:0;overflow:hidden;}
  body{width:1200px;height:496px;background:var(--stage);position:relative;font-family:"Montserrat",sans-serif;}
  .cover{position:absolute;top:48px;width:560px;height:400px;box-shadow:0 6px 24px rgba(0,0,0,.18);overflow:hidden;}
  .cover svg{display:block;}
  .back-cover{left:25px;background:var(--paper);}
  .front-cover{left:615px;background:var(--red);}
  .name-small{font-family:"Montserrat",sans-serif;font-weight:600;fill:var(--black);}
  .name-large{font-family:"Montserrat",sans-serif;font-weight:900;letter-spacing:2px;fill:var(--red);}
  .slogan{font-family:"Montserrat",sans-serif;font-weight:400;fill:var(--grey);letter-spacing:1px;}
  .contact-text{font-family:"Montserrat",sans-serif;font-size:8.5px;fill:var(--black);}
  .contact-label{fill:var(--red);font-weight:600;}
  .front-title{font-family:"Montserrat",sans-serif;font-weight:900;fill:var(--black);letter-spacing:1px;}
  .front-kicker{font-family:"Montserrat",sans-serif;font-weight:800;fill:var(--red);}
  .badge-name{font-family:"Montserrat",sans-serif;font-weight:800;fill:var(--red);}
</style>
</head>
<body>

<section class="cover back-cover" aria-label="Catalogue back cover">
  <svg width="560" height="400" viewBox="0 0 560 400">
    <defs>
      <linearGradient id="fadedFleet" x1="0" y1="0" x2="1" y2="0">
        <stop offset="0" stop-color="#ffffff"/>
        <stop offset="1" stop-color="#dcdcdc"/>
      </linearGradient>
      <linearGradient id="skylinePhoto" x1="0" y1="0" x2="0.4" y2="1">
        <stop offset="0" stop-color="#f1b8cc"/>
        <stop offset="0.45" stop-color="#d96d7e"/>
        <stop offset="1" stop-color="#f2b36b"/>
      </linearGradient>
    </defs>
    <rect class="faded-photo" x="220" y="130" width="340" height="200" fill="url(#fadedFleet)" opacity=".7" role="img" aria-label="Faded photograph of a fuel tanker truck"/>
    <polygon class="top-band" points="100,30 560,8 560,13 100,35" fill="var(--red)"/>
    <rect class="corner-bar" x="0" y="40" width="40" height="4" fill="var(--black)"/>

    <text class="name-small" x="520" y="62" font-size="16" text-anchor="end">Dune</text>
    <text class="name-large" x="520" y="92" font-size="28" text-anchor="end">HAULERS</text>
    <text class="slogan" x="520" y="110" font-size="10" text-anchor="end">Moving fuel forward</text>

    <rect class="feature-photo" x="180" y="150" width="200" height="150" rx="26" fill="url(#skylinePhoto)" role="img" aria-label="City skyline with fuel tanker trucks at sunset"/>
    <line x1="265" y1="130" x2="265" y2="320" stroke="var(--red)" stroke-width="2.5"/>
    <line x1="165" y1="225" x2="400" y2="225" stroke="var(--red)" stroke-width="2.5"/>

    <text class="contact-text" x="280" y="345" text-anchor="middle"><tspan class="contact-label">Contact:</tspan> 0410-2283650, 0412-7719034</text>
    <text class="contact-text" x="280" y="357" text-anchor="middle"><tspan class="contact-label">Address:</tspan> 14 Depot Road, Westgate Industrial Park</text>
    <text class="contact-text" x="280" y="369" text-anchor="middle"><tspan class="contact-label">Email:</tspan> hello@dunehaulers.example</text>

    <polygon class="bottom-band" points="300,388 560,378 560,384 300,394" fill="var(--red)"/>
    <rect class="corner-bar" x="0" y="390" width="60" height="4" fill="var(--black)"/>
  </svg>
</section>

<section class="cover front-cover" aria-label="Catalogue front cover">
  <svg width="560" height="400" viewBox="0 0 560 400">
    <defs>
      <linearGradient id="redField" x1="0" y1="0" x2="1" y2="1">
        <stop offset="0" stop-color="#ee2a2f"/>
        <stop offset="1" stop-color="#b90c14"/>
      </linearGradient>
      <linearGradient id="panelPhoto" x1="0" y1="0" x2="1" y2="1">
        <stop offset="0" stop-color="#f4c3d2"/>
        <stop offset="0.5" stop-color="#d55a6a"/>
        <stop offset="1" stop-color="#e9a45f"/>
      </linearGradient>
      <linearGradient id="redFleet" x1="0" y1="0" x2="0" y2="1">
        <stop offset="0" stop-color="#d61820"/>
        <stop offset="1" stop-color="#a70a11"/>
      </linearGradient>
    </defs>
    <rect width="560" height="400" fill="url(#redField)"/>
    <rect class="fleet-tint" x="0" y="200" width="330" height="200" fill="url(#redFleet)" opacity=".8" role="img" aria-label="Red-tinted photograph of tanker trucks"/>

    <g class="motion-panels" role="img" aria-label="Tanker trucks in front of a city skyline, split across slanted panels">
      <polygon points="170,30 240,22 300,230 235,238" fill="url(#panelPhoto)"/>
      <polygon points="250,20 330,12 390,220 310,228" fill="url(#panelPhoto)"/>
      <polygon points="340,11 430,3 490,210 400,219" fill="url(#panelPhoto)"/>
      <polygon points="440,2 540,-6 560,0 560,200 500,209" fill="url(#panelPhoto)"/>
    </g>
    <rect class="corner-bar" x="500" y="0" width="60" height="5" fill="var(--black)"/>

    <polygon class="badge-panel" points="20,45 150,30 150,150 40,170" fill="var(--paper)"/>
    <circle cx="88" cy="82" r="14" fill="var(--red)"/>
    <text class="badge-name" x="88" y="120" font-size="13" text-anchor="middle">Dune Haulers</text>

    <polygon class="title-band" points="200,250 560,210 560,360 228,372" fill="var(--paper)"/>
    <text class="front-kicker" x="250" y="268" font-size="18">Dune</text>
    <text class="front-title" x="245" y="322" font-size="52">HAULERS</text>
    <text class="slogan" x="540" y="350" font-size="12" text-anchor="end">Moving fuel forward</text>
    <rect class="corner-bar" x="500" y="368" width="60" height="5" fill="var(--black)"/>
  </svg>
</section>

</body>
</html>
```